Postcard Design

we need a post card design for our company in worth, illinois called Velmora Dental lab we would like to see designs that use the colors blue and gray. We are a dental lab specializing in removable dentures and partials. These particular post cards are emphasizing doing relines and repairs the same day our address is 48207 N Cobbet ave worth I'll. Phone 708-555-0194

Industry/Entity Type

Dental

```html
<!DOCTYPE html>
<html lang="en">
<head>
<meta charset="utf-8">
<title>Velmora Dental Lab – Postcard</title>
<link rel="stylesheet" href="https://fonts.googleapis.com/css2?family=Roboto+Condensed:wght@700&family=Arimo:ital,wght@0,700;1,700&family=Open+Sans:ital,wght@0,400;1,700&display=swap">
<style>
  :root {
    --navy: #0b4f8c;
    --deep-blue: #063f78;
    --mid-blue: #0c6aa8;
    --sky-blue: #2a8fd0;
    --ice: #dff3fb;
    --text-blue: #1b5fa8;
    --photo-gray: #d9dcdf;
    --photo-light: #f2f3f4;
    --cream: #fbf4d9;
    --white: #ffffff;
    --ink: #222;
  }
  html, body {
    margin: 0;
    padding: 0;
    width: 786px;
    height: 1200px;
    overflow: hidden;
    background: var(--white);
  }
  .sheet { position: relative; width: 786px; height: 1200px; }

  .card {
    position: absolute;
    overflow: hidden;
    background: var(--white);
    outline: 1px solid #d5d5d5;
  }
  .card--front { left: 34px; top: 34px; width: 722px; height: 552px; }
  .card--back  { left: 31px; top: 610px; width: 722px; height: 560px; }

  .card__art { position: absolute; inset: 0; }

  .headline {
    position: absolute;
    left: 300px; top: 232px; width: 380px;
    margin: 0;
    text-align: center;
    font: 700 31px/1.3 "Roboto Condensed", sans-serif;
    color: var(--text-blue);
    -webkit-text-stroke: 0.6px var(--white);
    paint-order: stroke fill;
  }
  .brand {
    position: absolute;
    left: 20px; top: 398px; width: 360px;
    text-align: center;
    color: var(--ice);
    font-family: "Roboto Condensed", sans-serif;
    font-weight: 700;
  }
  .brand__name { display: block; font-size: 45px; line-height: 1.1; }
  .brand__phone { display: block; font-size: 35px; line-height: 1.3; }

  .offer {
    position: absolute;
    left: 390px; top: 396px; width: 310px;
    text-align: center;
    color: var(--white);
    font-family: "Arimo", sans-serif;
    font-weight: 700;
  }
  .offer__lead { display: block; font-size: 29px; font-style: italic; line-height: 1.15; }
  .offer__detail { display: block; font-size: 20px; line-height: 1.4; }
  .offer__address { display: block; font-size: 18px; font-weight: 400; margin-top: 16px; }

  .hero-photo {
    position: absolute;
    left: 17px; top: 10px; width: 350px; height: 146px;
    background: linear-gradient(90deg, #e9e2da 0%, #f4f1ee 45%, #f6d9d5 75%, #f3f3f3 100%);
  }
  .pitch {
    position: absolute;
    left: 30px; top: 178px; width: 320px;
    margin: 0;
    text-align: center;
    font: 400 15px/1.5 "Open Sans", sans-serif;
    color: var(--text-blue);
  }
  .pitch__cta { display: block; font-style: italic; font-weight: 700; color: var(--navy); }
  .sign-off {
    position: absolute;
    left: 10px; top: 312px; width: 360px;
    text-align: center;
    font-family: "Roboto Condensed", sans-serif;
    font-weight: 700;
    color: var(--navy);
  }
  .sign-off__name { display: block; font-size: 40px; line-height: 1.15; }
  .sign-off__phone { display: block; font-size: 34px; line-height: 1.35; }

  .return-address {
    position: absolute;
    left: 428px; top: 34px;
    margin: 0;
    font: 400 13px/1.5 "Open Sans", sans-serif;
    color: var(--ink);
    font-style: normal;
  }
</style>
</head>
<body>
<main class="sheet">

  <section class="card card--front">
    <svg class="card__art" width="722" height="552" viewBox="0 0 722 552" aria-hidden="false">
      <defs>
        <linearGradient id="lab-photo" x1="0" y1="0" x2="1" y2="1">
          <stop offset="0" stop-color="var(--photo-light)"/>
          <stop offset="0.55" stop-color="var(--photo-gray)"/>
          <stop offset="1" stop-color="#e8c9c4"/>
        </linearGradient>
        <linearGradient id="band-deep" x1="0" y1="0" x2="1" y2="0">
          <stop offset="0" stop-color="var(--deep-blue)"/>
          <stop offset="1" stop-color="var(--mid-blue)"/>
        </linearGradient>
      </defs>
      <rect role="img" aria-label="Photo: gloved hands trimming a denture model on a dental articulator" x="0" y="0" width="722" height="360" fill="url(#lab-photo)"/>
      <path d="M0 246 C 200 300, 480 340, 722 318 L722 552 L0 552 Z" fill="var(--cream)"/>
      <path d="M0 252 C 200 306, 480 348, 722 328 L722 552 L0 552 Z" fill="var(--sky-blue)"/>
      <path d="M0 296 C 220 340, 480 362, 722 350 L722 552 L0 552 Z" fill="url(#band-deep)"/>
    </svg>

    <h1 class="headline">We specialize in removable dentures and partials.</h1>

    <div class="brand">
      <span class="brand__name">Velmora Dental Lab</span>
      <span class="brand__phone">(708) 555-0194</span>
    </div>

    <p class="offer">
      <span class="offer__lead">SAME DAY</span>
      <span class="offer__detail">RELINES AND REPAIRS!</span>
      <span class="offer__address">48207 Cobbet Ave, Worth, IL 60482</span>
    </p>
  </section>

  <section class="card card--back">
    <div class="hero-photo" role="img" aria-label="Photo: smiling senior couple beside a set of full dentures"></div>

    <svg class="card__art" width="722" height="560" viewBox="0 0 722 560" aria-hidden="true">
      <defs>
        <linearGradient id="swoosh" x1="0" y1="0" x2="1" y2="0">
          <stop offset="0" stop-color="var(--navy)"/>
          <stop offset="0.5" stop-color="var(--sky-blue)"/>
          <stop offset="1" stop-color="#8fd0f2"/>
        </linearGradient>
      </defs>
      <path d="M370 0 L420 0 C 438 140, 430 330, 396 475 L370 475 C 402 330, 404 150, 370 0 Z" fill="url(#swoosh)"/>
    </svg>

    <p class="pitch">
      There’s no acceptable way to cut corners when working with dentures. That’s why we don’t. Turn to Velmora Dental Lab for removables solutions - for high quality work at reasonable prices.
      <span class="pitch__cta">Call us to discuss your first case!</span>
    </p>

    <div class="sign-off">
      <span class="sign-off__name">Velmora Dental Lab</span>
      <span class="sign-off__phone">(708) 555-0194</span>
    </div>

    <address class="return-address">
      Velmora Dental Lab<br>
      48207 N Cobbet Ave<br>
      Worth, IL 60482
    </address>
  </section>

</main>
</body>
</html>
```